RK Bastone Construction Inc.

Design a new business card for our construction company
To be removed from current card:
Delete 25 years
Delete Tenant fit up Renovations section

```html
<!DOCTYPE html>
<html lang="en">
<head>
<meta charset="utf-8">
<title>RK Bastone Construction Inc. – Business Card</title>
<link rel="stylesheet" href="https://fonts.googleapis.com/css2?family=Exo+2:wght@400;500;700;800&display=swap">
<style>
  :root {
    --purple: #562f75;
    --teal: #237a70;
    --white: #ffffff;
    --backdrop: #262626;
  }
  * { box-sizing: border-box; margin: 0; padding: 0; }
  html, body {
    width: 1200px;
    height: 1015px;
    overflow: hidden;
    background: var(--backdrop);
    font-family: "Exo 2", sans-serif;
  }
  .sheet {
    width: 1200px;
    height: 1015px;
    display: flex;
    flex-direction: column;
    align-items: center;
    justify-content: center;
    gap: 60px;
  }
  .card {
    position: relative;
    width: 700px;
    height: 400px;
    overflow: hidden;
    box-shadow: 0 10px 30px rgba(0,0,0,.5);
  }

  /* Back of card */
  .card--back { background: var(--purple); }
  .card--back .wordmark {
    position: absolute;
    left: 0; right: 0; top: 78px;
    text-align: center;
    color: var(--white);
  }
  .card--back .service-band {
    position: absolute;
    left: 0; right: 0; top: 250px;
    height: 66px;
    background: var(--teal);
    display: flex;
    align-items: center;
    justify-content: center;
    color: var(--white);
    font-weight: 800;
    font-size: 20px;
    letter-spacing: 3px;
    text-transform: uppercase;
  }
  .service-band .sep { margin: 0 14px; font-weight: 400; }

  .wordmark { font-weight: 700; line-height: 1; }
  .wordmark .wordmark-name {
    display: block;
    font-size: 72px;
    letter-spacing: 1px;
    text-transform: uppercase;
  }
  .wordmark .wordmark-sub {
    display: block;
    font-size: 27px;
    letter-spacing: 9px;
    text-transform: uppercase;
    margin-top: 8px;
  }

  /* Front of card */
  .card--front { background: var(--white); }
  .card--front .wordmark {
    position: absolute;
    left: 0; right: 0; top: 48px;
    text-align: center;
    color: var(--teal);
  }
  .card--front .holder-name {
    position: absolute;
    left: 0; right: 0; top: 190px;
    text-align: center;
    color: var(--teal);
    font-weight: 800;
    font-size: 24px;
    letter-spacing: 3px;
    text-transform: uppercase;
  }
  .contact-band {
    position: absolute;
    left: 0; right: 0; top: 232px;
    height: 104px;
    background: var(--teal);
    display: flex;
    align-items: center;
    justify-content: center;
    color: var(--white);
    font-size: 17px;
    font-weight: 500;
  }
  .contact-col { display: flex; flex-direction: column; gap: 8px; }
  .contact-col--online { align-items: flex-end; padding-right: 20px; }
  .contact-col--phone { align-items: flex-start; padding-left: 20px; }
  .contact-divider { width: 1px; height: 62px; background: rgba(255,255,255,.7); }
  .contact-item { display: flex; align-items: center; gap: 9px; }
  .contact-item svg { width: 18px; height: 18px; flex: none; }
  .address-band {
    position: absolute;
    left: 0; right: 0; bottom: 0;
    height: 64px;
    background: var(--purple);
    display: flex;
    align-items: center;
    justify-content: center;
    color: var(--white);
    font-size: 19px;
    font-weight: 500;
    letter-spacing: .5px;
  }
</style>
</head>
<body>
<main class="sheet">

  <section class="card card--back" aria-label="Business card back">
    <div class="wordmark">
      <span class="wordmark-name">RK Bastone</span>
      <span class="wordmark-sub">Construction Inc.</span>
    </div>
    <div class="service-band">
      <span>Office</span><span class="sep">|</span><span>Retail</span><span class="sep">|</span><span>Institutional</span>
    </div>
  </section>

  <section class="card card--front" aria-label="Business card front">
    <div class="wordmark">
      <span class="wordmark-name">RK Bastone</span>
      <span class="wordmark-sub">Construction Inc.</span>
    </div>
    <p class="holder-name">Leo Bastone</p>

    <div class="contact-band">
      <div class="contact-col contact-col--online">
        <div class="contact-item">
          <span>leo@rkbastoneconst.ca</span>
          <svg viewBox="0 0 24 24" fill="none" stroke="currentColor" stroke-width="2"><rect x="2" y="5" width="20" height="14"/><path d="M2 5l10 8 10-8"/></svg>
        </div>
        <div class="contact-item">
          <span>www.rkbastoneconstruction.ca</span>
          <svg viewBox="0 0 24 24" fill="none" stroke="currentColor" stroke-width="2"><circle cx="12" cy="12" r="10"/><path d="M2 12h20M12 2c3 3 3 17 0 20M12 2c-3 3-3 17 0 20"/></svg>
        </div>
      </div>
      <div class="contact-divider"></div>
      <div class="contact-col contact-col--phone">
        <div class="contact-item">
          <svg viewBox="0 0 24 24" fill="none" stroke="currentColor" stroke-width="2"><path d="M5 3h4l2 5-3 2a11 11 0 0 0 6 6l2-3 5 2v4a2 2 0 0 1-2 2A17 17 0 0 1 3 5a2 2 0 0 1 2-2z"/></svg>
          <span>613-555-0142 ext.221</span>
        </div>
        <div class="contact-item">
          <svg viewBox="0 0 24 24" fill="none" stroke="currentColor" stroke-width="2"><rect x="6" y="2" width="12" height="20" rx="2"/><path d="M11 18h2"/></svg>
          <span>613-555-0187</span>
        </div>
      </div>
    </div>

    <div class="address-band">2180 Millbrook Rd., Suite 100. Ottawa, On K1B 4T7</div>
  </section>

</main>
</body>
</html>
```